Halvey’s

I would like a high class looking card with my logo and contact details (as per uploaded) Elegant, professional and highest quality feel

The following text included …..
“All commercial and residential painting work, large or small. Highest quality finishes and service.”

Industry/Entity Type

Painting

Contact Information for Business Card

Name, phone number, address, email address, company logo

Requirements
Must have
• Double sided

```html
<!DOCTYPE html>
<html lang="en">
<head>
<meta charset="utf-8">
<title>Halvey’s — Business Card</title>
<link rel="stylesheet" href="https://fonts.googleapis.com/css2?family=Cinzel:wght@400;500&family=Libre+Baskerville&family=Lato:wght@400;700&display=swap">
<style>
  :root {
    --backdrop: #141414;
    --card: #1c1c1c;
    --gold: #b3834a;
    --silver: #a9a9a9;
    --circle: #262626;
  }
  * { box-sizing: border-box; margin: 0; padding: 0; }
  html, body { width: 1200px; height: 800px; overflow: hidden; }
  body {
    background: var(--backdrop);
    display: flex;
    align-items: center;
    justify-content: center;
    gap: 40px;
  }
  .card {
    position: relative;
    width: 540px;
    height: 310px;
    background: var(--card);
    border-radius: 22px;
    overflow: hidden;
  }

  /* Contact side */
  .identity {
    position: absolute;
    left: 40px;
    top: 92px;
    width: 230px;
    text-align: right;
  }
  .identity__name {
    font-family: "Cinzel", serif;
    font-weight: 500;
    font-size: 27px;
    letter-spacing: 0.5px;
    color: var(--gold);
    line-height: 1;
  }
  .identity__role {
    font-family: "Lato", sans-serif;
    font-size: 15px;
    color: var(--gold);
    margin-top: 4px;
  }
  .divider {
    position: absolute;
    left: 292px;
    top: 70px;
    width: 1px;
    height: 98px;
    background: var(--gold);
  }
  .contact {
    position: absolute;
    left: 312px;
    top: 70px;
    list-style: none;
    font-family: "Lato", sans-serif;
    color: var(--gold);
    font-size: 13px;
    line-height: 1.35;
  }
  .contact__item { display: flex; gap: 8px; margin-bottom: 3px; }
  .contact__icon { width: 11px; height: 11px; margin-top: 3px; flex: none; fill: var(--gold); }
  .contact__phone { font-weight: 700; font-size: 17px; }
  .contact__phone .contact__icon { margin-top: 5px; }
  .services {
    position: absolute;
    left: 0;
    right: 0;
    bottom: 58px;
    text-align: center;
    font-family: "Libre Baskerville", serif;
    font-size: 12.5px;
    line-height: 1.6;
    color: var(--gold);
  }

  /* Brand side */
  .brand {
    position: absolute;
    inset: 0;
    display: flex;
    align-items: center;
    justify-content: center;
    gap: 22px;
  }
  .brand__name {
    font-family: "Cinzel", serif;
    font-weight: 400;
    font-size: 50px;
    letter-spacing: 2px;
    color: var(--silver);
  }
  .brand__circle {
    width: 84px;
    height: 84px;
    border-radius: 50%;
    background: var(--circle);
  }
</style>
</head>
<body>
  <section class="card card--contact">
    <div class="identity">
      <p class="identity__name">Daniel Halvey</p>
      <p class="identity__role">Owner</p>
    </div>
    <div class="divider"></div>
    <ul class="contact">
      <li class="contact__item">
        <svg class="contact__icon" viewBox="0 0 12 12" aria-hidden="true"><path d="M6 0a4 4 0 0 0-4 4c0 3 4 8 4 8s4-5 4-8a4 4 0 0 0-4-4zm0 5.6A1.6 1.6 0 1 1 6 2.4a1.6 1.6 0 0 1 0 3.2z"/></svg>
        <span>42 Kowhai Terrace<br>Taupaki, 3188</span>
      </li>
      <li class="contact__item contact__phone">
        <svg class="contact__icon" viewBox="0 0 12 12" aria-hidden="true"><path d="M2.5 0.5l2 2.2-1 1.4c.6 1.5 1.8 2.7 3.3 3.4l1.4-1 2.3 2-1.3 2.2C5 10.6 1.2 6.8.4 2.2z"/></svg>
        <span>021 555 0147</span>
      </li>
      <li class="contact__item">
        <svg class="contact__icon" viewBox="0 0 12 12" aria-hidden="true"><path d="M0 2h12v8H0zM.8 2.6 6 6.6l5.2-4H.8z"/></svg>
        <span>daniel@halveyspainters.com</span>
      </li>
    </ul>
    <p class="services">All commercial and residential painting work,<br>large or small. Highest quality finishes and service.</p>
  </section>

  <section class="card card--brand">
    <div class="brand">
      <span class="brand__name">Halvey’s</span>
      <span class="brand__circle" aria-hidden="true"></span>
    </div>
  </section>
</body>
</html>
```